Web Design Project - Coral Reef Licensing Limited

Coral Reef Licensing Limited is a Vanuatu based License and Compliance Consultant to the Vanuatu Government. We are authorised to review and recommend on all applications for Interactive Gaming Licenses (On Line Casino and Sports/Horse Racing) for the Vanuatu Government.
We need a professional web site that presents us a professional organisation while eye-catching in the same breath.
Examples of some similar operations include:
http://www.northbayloreth.com/html/home.php
http://wagering.qx.example/
http://www.placesopen.example/egaming
We are looking for the final product in code, not PSD please.
Hi all.
We are looking for the project to be a final site, not just PSD please.
Thanks all.
Derek
Target Market(s)
The target market are corporate bookmakers, on line casino and on line poker operators (Interactive Gaming).
in addition we are the first point of contact for anyone looking to Vanuatu as a potential location for licensing.
Industry/Entity Type
Casino
Colors
Designer to choose colors to be used in the design.
Requirements
Must have
- They key things for this site are:
Clear navigation - Needs to be simple and fast to navigate
Visually appealing and simple home page - Speaks for itself
Prominent Contact Information - One of the most important components
FAQ’s - Simple and easy to access such as "who we are, what we do and stored documents"
The site must have the following pages:
Main
Who Are We
Document Repository (12-15 pdf''s)
Reference and links back to the Regulatory Body and relevant pages being:
https://dutiesandlevies.example/index.php/en/inland-revenue/rates-taxes/interactive-gaming-license-tax
and
https://dutiesandlevies.example/index.php/en/inland-revenue/rates-taxes
Contact Us

```html
<!DOCTYPE html>
<html lang="en">
<head>
<meta charset="utf-8">
<title>Coral Reef Licensing Limited</title>
<link rel="stylesheet" href="https://fonts.googleapis.com/css2?family=Catamaran:wght@400;500;600;700&family=Open+Sans:wght@400;600&display=swap">
<style>
  :root {
    --black: #000000;
    --white: #ffffff;
    --gold-light: #e9b421;
    --gold: #d99a12;
    --gold-dark: #b06d06;
    --band-top: #8a5a04;
    --heading: #222222;
    --body: #6a6a6a;
    --news-gold: #c8860f;
    --date-gold: #b98b2c;
    --rule: #e4e4e4;
    --btn-dark-top: #5b5b5b;
    --btn-dark-bottom: #2c2c2c;
  }
  * { margin: 0; padding: 0; box-sizing: border-box; }
  html, body { width: 1200px; height: 1158px; overflow: hidden; background: var(--white); }
  body { font-family: "Open Sans", sans-serif; color: var(--body); }
  .page { position: relative; width: 1200px; height: 1158px; overflow: hidden; }

  .site-header { position: absolute; left: 0; top: 0; width: 1200px; height: 155px; background: var(--black); }
  .brand { position: absolute; left: 155px; top: 34px; font-family: "Catamaran", sans-serif; font-weight: 600; font-size: 24px; line-height: 26px; color: var(--white); letter-spacing: 0.5px; }
  .social { position: absolute; left: 719px; top: 58px; display: flex; gap: 2px; }
  .social span { width: 30px; height: 30px; border-radius: 50%; background: var(--white); border: 2px solid #cfcfcf; display: block; }
  .search { position: absolute; left: 829px; top: 58px; width: 216px; height: 30px; border-radius: 15px; background: #1e1e1e; border: 1px solid #4a4a4a; }
  .search span { position: absolute; left: 15px; top: 6px; font-size: 11.5px; color: #8c8c8c; }
  .search svg { position: absolute; right: 11px; top: 7px; }

  .band { position: absolute; left: 0; top: 155px; width: 1200px; height: 320px; background: linear-gradient(to bottom, var(--band-top), #b88a3c 45%, var(--white)); }

  .main-nav { position: absolute; left: 153px; top: 105px; width: 894px; height: 50px; background: linear-gradient(to bottom, var(--gold-light), var(--gold-dark)); display: flex; }
  .main-nav a { display: block; height: 50px; line-height: 52px; padding: 0 18px; color: var(--white); text-decoration: none; font-family: "Catamaran", sans-serif; font-weight: 500; font-size: 16.5px; border-right: 1px solid rgba(255,255,255,0.25); }
  .main-nav a:first-child { padding-left: 37px; }

  .hero { position: absolute; left: 153px; top: 155px; width: 894px; height: 366px; background: radial-gradient(ellipse at 50% 70%, #2e9a6a 0%, #1d6e4c 40%, #2a1a0c 85%); }
  .hero::after { content: ""; position: absolute; left: 0; right: 0; bottom: 0; height: 110px; background: linear-gradient(to bottom, rgba(255,255,255,0), var(--white)); }
  .dots { position: absolute; left: 576px; top: 492px; display: flex; gap: 3px; z-index: 2; }
  .dots span { width: 13px; height: 13px; border-radius: 50%; background: #3a3a3a; display: block; }

  .welcome { position: absolute; left: 155px; top: 552px; width: 420px; }
  .welcome h1 { font-family: "Catamaran", sans-serif; font-weight: 600; font-size: 28px; color: var(--heading); line-height: 34px; margin-bottom: 10px; }
  .welcome p { font-size: 11.8px; line-height: 19px; margin-bottom: 5px; }
  .btn-light { position: absolute; left: 154px; top: 704px; width: 108px; height: 31px; border: 1px solid #cfcfcf; border-radius: 3px; background: linear-gradient(#ffffff, #ececec); color: #444; font-family: "Catamaran", sans-serif; font-weight: 500; font-size: 14px; line-height: 31px; text-align: center; }

  .card { position: absolute; top: 555px; width: 216px; height: 181px; border-radius: 3px; overflow: visible; }
  .card .photo { height: 114px; border-radius: 3px 3px 0 0; }
  .card .info { height: 67px; background: linear-gradient(to bottom, var(--gold), var(--gold-dark)); border-radius: 0 0 3px 3px; padding: 10px 0 0 15px; color: var(--white); }
  .card h3 { font-family: "Catamaran", sans-serif; font-weight: 600; font-size: 17.5px; line-height: 20px; }
  .card p { font-size: 10.5px; margin-top: 4px; color: #fbe6b8; }
  .card::after { content: ""; position: absolute; left: 12px; right: 12px; bottom: -12px; height: 12px; background: radial-gradient(ellipse at 50% 0%, rgba(0,0,0,0.25), rgba(0,0,0,0) 70%); }
  .card-license { left: 603px; }
  .card-license .photo { background: linear-gradient(135deg, #8c8f95, #5a4a3a 55%, #b8b0a4); }
  .card-review { left: 830px; }
  .card-review .photo { background: linear-gradient(135deg, #3a2a24, #8a6450 50%, #2b3a45); }

  .rule { position: absolute; left: 153px; top: 788px; width: 894px; height: 1px; background: var(--rule); }

  .news-title { position: absolute; left: 153px; top: 823px; font-family: "Catamaran", sans-serif; font-weight: 400; font-size: 24px; color: var(--news-gold); }
  .news-item { position: absolute; top: 868px; width: 280px; }
  .news-item time { display: block; font-size: 12px; color: var(--date-gold); margin-bottom: 4px; }
  .news-item p { font-size: 11.8px; line-height: 19px; }
  .news-item a { display: block; margin-top: 6px; font-family: "Catamaran", sans-serif; font-weight: 500; font-size: 13px; color: var(--black); text-decoration: none; }
  .news-one { left: 154px; }
  .news-two { left: 454px; }

  .docs { position: absolute; left: 775px; top: 823px; width: 275px; }
  .docs h2 { font-family: "Catamaran", sans-serif; font-weight: 400; font-size: 24px; color: var(--heading); line-height: 32px; margin-bottom: 8px; }
  .docs p { font-size: 11.3px; line-height: 19px; margin-bottom: 5px; }
  .btn-dark { position: absolute; left: 776px; top: 955px; width: 109px; height: 32px; border-radius: 3px; background: linear-gradient(var(--btn-dark-top), var(--btn-dark-bottom)); color: var(--white); font-family: "Catamaran", sans-serif; font-weight: 500; font-size: 14px; line-height: 33px; text-align: center; }

  .site-footer { position: absolute; left: 0; top: 1036px; width: 1200px; height: 122px; background: var(--black); }
  .footer-nav { position: absolute; left: 154px; top: 33px; font-family: "Catamaran", sans-serif; font-weight: 600; font-size: 15px; color: var(--white); }
  .footer-nav a { color: var(--white); text-decoration: none; }
  .footer-nav .sep { margin: 0 7px; }
  .copyright { position: absolute; left: 154px; top: 61px; font-size: 11px; color: #9a9a9a; }
  .partner { position: absolute; left: 770px; top: 30px; display: flex; align-items: center; gap: 8px; }
  .partner span.mark { width: 34px; height: 34px; border-radius: 50%; background: #8a7a4a; display: block; }
  .partner span.name { font-family: "Catamaran", sans-serif; font-weight: 600; font-size: 13px; line-height: 15px; color: var(--white); width: 200px; }
</style>
</head>
<body>
<div class="page">
  <div class="band"></div>

  <header class="site-header">
    <div class="brand">Coral Reef Licensing<br>Limited</div>
    <div class="social" aria-label="Social links">
      <span></span><span></span><span></span>
    </div>
    <div class="search">
      <span>Search here</span>
      <svg width="17" height="17" viewBox="0 0 17 17"><circle cx="7" cy="7" r="5.5" fill="none" stroke="#8c8c8c" stroke-width="2"/><line x1="11" y1="11" x2="15.5" y2="15.5" stroke="#8c8c8c" stroke-width="2" stroke-linecap="round"/></svg>
    </div>
  </header>

  <nav class="main-nav">
    <a href="#">HOME</a>
    <a href="#">WHO ARE WE</a>
    <a href="#">DOCUMENTS REPOSITORY</a>
    <a href="#">REFERENCES</a>
    <a href="#">CONTACT US</a>
  </nav>

  <div class="hero" role="img" aria-label="Casino roulette table with slot machines in the background"></div>
  <div class="dots"><span></span><span></span><span></span><span></span></div>

  <section class="welcome">
    <h1>WELCOME</h1>
    <p>Mauris vel lacus vitae felis vestibulum volutpat Etiam est nunc venenatis in tristique eu imperdiet ac nisl Cum sociis natoque penatibus et magnis dis parturient montes nascetur ridiculus mus In iaculis</p>
    <p>Facilisis massa Etiam eu urna Sed porta Suspendisse quam leo molestie sed luctus quis feugiat in pede Fusce tellus Sed metus augue</p>
  </section>
  <div class="btn-light">READ MORE</div>

  <article class="card card-license">
    <div class="photo" role="img" aria-label="Jockeys racing horses on a track"></div>
    <div class="info"><h3>LICENSE &amp; COMPLIANCE</h3><p>Etiam est nunc venenatis in tristique</p></div>
  </article>
  <article class="card card-review">
    <div class="photo" role="img" aria-label="Group of players celebrating at a casino table"></div>
    <div class="info"><h3>REVIEW &amp; SUPPORT</h3><p>Etiam est nunc venenatis in tristique</p></div>
  </article>

  <div class="rule"></div>

  <h2 class="news-title">Latest News</h2>
  <article class="news-item news-one">
    <time>October 23, 2014</time>
    <p>Morbi porta libero id ullamcorper nonummy nibh ligula pulvinar metus eget consectetueFusce tellus Sed metus augue convallis et vehicula ut</p>
    <a href="#">LEARN MORE</a>
  </article>
  <article class="news-item news-two">
    <time>October 25, 2014</time>
    <p>Morbi porta libero id ullamcorper nonummy nibh ligula pulvinar metus eget consectetueFusce tellus Sed metus augue convallis et vehicula ut</p>
    <a href="#">LEARN MORE</a>
  </article>

  <section class="docs">
    <h2>Documents Repository</h2>
    <p>Mauris vel lacus vitae felis vestibulum volutpat Etiam est nunc venenatis in tristique eu imperdiet ac nisl Cum sociis natoque penatibus</p>
    <p>et magnis dis parturient montes nascetur</p>
  </section>
  <div class="btn-dark">READ MORE</div>

  <footer class="site-footer">
    <div class="footer-nav">
      <a href="#">Home</a><span class="sep">|</span><a href="#">Who are We</a><span class="sep">|</span><a href="#">Documents Repository</a><span class="sep">|</span><a href="#">References</a><span class="sep">|</span><a href="#">Contact us</a>
    </div>
    <div class="copyright">© 2014 Company Name &nbsp;All right reserved &nbsp;Term of Use</div>
    <div class="partner">
      <span class="mark"></span>
      <span class="name">Harbour Duties &amp; Levies Department</span>
    </div>
  </footer>
</div>
</body>
</html>
```